Copper Ridge Harbor Home Inc. Website Update

We have a couple of broken links such as the "contact us" and would like to add board members and a calendar of events. We are open to a new design.

```html
<!DOCTYPE html>
<html lang="en">
<head>
<meta charset="utf-8">
<title>Copper Ridge Harbor Home Inc.</title>
<link href="https://fonts.googleapis.com/css2?family=Barlow:wght@400;500;600;700&family=Lato:wght@400;700&display=swap" rel="stylesheet">
<style>
:root{
  --rose:#c48a9c;
  --rose-soft:#cfa6b2;
  --mauve:#b79aaa;
  --gold:#c6ad74;
  --sand:#dccaa4;
  --tan:#d3b597;
  --slate:#8f909b;
  --ink:#2f2f33;
  --text:#555;
  --muted:#8a8a8a;
  --line:#ddd;
  --paper:#f3f3f3;
  --footer:#3a3d43;
  --white:#fff;
}
*{box-sizing:border-box;margin:0;padding:0}
html,body{width:1200px;height:4557px;overflow:hidden}
body{font-family:'Lato',sans-serif;color:var(--text);background:var(--white);position:relative}
h1,h2,h3,h4,.nav a,.btn{font-family:'Barlow',sans-serif}
section,header,footer{position:absolute;left:0;width:1200px}
.abs{position:absolute}
.ph{background:linear-gradient(135deg,#b9a48f,#8e7b70 50%,#cdb9a6)}

/* header */
.site-header{top:0;height:120px;background:var(--white);z-index:3}
.brand{left:172px;top:12px;width:165px;height:165px;border-radius:50%;background:var(--white);border:5px solid var(--rose);display:flex;align-items:center;justify-content:center;text-align:center;font-family:'Barlow',sans-serif;font-weight:600;font-size:17px;line-height:1.2;color:var(--rose);padding:18px}
.topbar{right:170px;top:10px;display:flex;align-items:center;gap:22px;font-family:'Barlow',sans-serif;font-size:14px;font-weight:600;color:var(--ink)}
.topbar .phone{display:flex;align-items:center;gap:8px}
.donate{background:var(--rose-soft);color:var(--white);padding:6px 16px;border-radius:14px;font-size:13px}
.nav{right:170px;top:72px;display:flex;gap:16px}
.nav a{font-size:13px;font-weight:600;color:var(--ink);text-decoration:none;letter-spacing:.2px;white-space:nowrap}

/* hero */
.hero{top:120px;height:660px}
.hero .ph{width:100%;height:100%;background:linear-gradient(160deg,#6d8a4e,#c69c86 35%,#9aa8c4 60%,#5f7a45)}
.hero svg{position:absolute;left:0;bottom:0}

/* intro */
.intro{top:780px;height:315px;background:var(--paper)}
.intro-card{top:40px;width:470px;height:180px}
.intro-card h2{font-size:34px;font-weight:600;color:var(--gold);letter-spacing:1px}
.intro-card p{font-size:12px;line-height:1.5;margin-top:8px;width:230px}
.intro .circle{width:180px;height:180px;border-radius:50%;border:6px solid var(--white);box-shadow:0 2px 8px rgba(0,0,0,.2)}
.btn{display:inline-block;background:var(--sand);color:var(--white);font-size:11px;font-weight:600;padding:7px 18px;border-radius:14px;margin-top:18px;letter-spacing:.5px}

/* about */
.about{top:1095px;height:570px}
.about h2{left:175px;top:160px;font-size:34px;font-weight:600;color:var(--ink);line-height:1.15}
.about .lead{left:175px;top:250px;width:410px;font-size:15px;line-height:1.5;color:var(--muted)}
.about .body{left:175px;top:315px;width:410px;font-size:12px;line-height:1.55}
.service{width:176px;height:176px;border:1.5px solid var(--rose);display:flex;flex-direction:column;align-items:center;justify-content:center;text-align:center;font-family:'Barlow',sans-serif;font-size:15px;color:var(--ink);gap:14px;line-height:1.25}

/* board */
.board{top:1640px;height:700px;background:var(--paper)}
.sec-title{width:100%;text-align:center;font-size:30px;font-weight:600;color:var(--ink);letter-spacing:.5px}
.sec-sub{width:100%;text-align:center;font-size:15px;line-height:1.55;color:var(--muted)}
.member{width:200px;text-align:center}
.member .portrait{width:166px;height:166px;border-radius:50%;margin:0 auto;border:5px solid var(--white);box-shadow:0 0 0 1.5px #bbb}
.member h4{font-size:15px;font-weight:500;color:var(--gold);margin-top:22px}
.member p{font-size:12px;line-height:1.55;margin-top:10px}
.chev{font-size:40px;color:#999;font-family:'Barlow',sans-serif}

/* calendar */
.events{top:2340px;height:812px}
.card{top:230px;width:253px;height:455px;border:1px solid var(--line);background:var(--white)}
.cal-head{height:210px;background:linear-gradient(180deg,#c2a9b6,#a98a9b);text-align:center;color:var(--white);padding-top:55px}
.cal-head h3{font-size:32px;font-weight:600}
.cal-head .yr{font-size:13px}
.cal-head .add{display:inline-block;border:1px solid rgba(255,255,255,.6);padding:6px 12px;font-family:'Barlow',sans-serif;font-size:13px;margin-top:18px}
.cal-grid{display:grid;grid-template-columns:repeat(7,1fr);padding:14px 14px 0;row-gap:16px;text-align:center;font-size:14px;color:var(--ink)}
.cal-grid .dn{font-size:10px;color:var(--muted);font-weight:700}
.cal-grid .o{color:#bbb}
.card .ph{height:210px}
.card h4{font-size:17px;font-weight:500;color:var(--ink);padding:24px 20px 0;line-height:1.3}
.card p{font-size:12px;line-height:1.55;padding:12px 20px 0}
.date{display:inline-block;margin:18px 20px 0;background:var(--mauve);color:var(--white);font-size:11px;padding:6px 14px}

/* voices & join */
.voices{top:3152px;height:528px;width:600px;background:var(--slate);color:var(--white)}
.join{top:3152px;left:600px;height:528px;width:600px;background:var(--tan);color:var(--white)}
.voices h2,.join h2{font-size:30px;font-weight:500;letter-spacing:.5px}
.voices .intro-txt,.join .intro-txt{font-size:12px;line-height:1.6;opacity:.85}
.quote{font-size:13px;line-height:1.6}
.job{width:225px;height:170px;border:2px solid var(--white);background:rgba(180,130,100,.45);text-align:center;padding-top:46px}
.job h4{font-size:18px;font-weight:600;line-height:1.2}
.job p{font-size:11px;margin-top:10px;line-height:1.4}

/* contact */
.contact{top:3680px;height:520px}
.contact h2{top:78px}
.contact .sec-sub{top:125px;width:420px;left:390px;font-size:12px}
.form{left:390px;top:190px;width:420px}
.field{font-size:12px;color:var(--ink);padding-bottom:12px;border-bottom:1px solid #ccc;margin-bottom:18px}
.submit{left:548px;top:390px;width:108px;height:42px;border-radius:21px;background:var(--rose-soft);color:var(--white);font-family:'Barlow',sans-serif;font-weight:600;font-size:14px;display:flex;align-items:center;justify-content:center}
.contact .person{left:825px;top:20px;width:310px;height:500px;background:linear-gradient(180deg,#6b4a3c,#2a2a30 60%,#1e1f24);border-radius:150px 150px 0 0}

/* footer */
.site-footer{top:4110px;height:447px}
.site-footer svg{position:absolute;top:0;left:0}
.foot-body{top:55px;height:392px;width:1200px;background:var(--footer);color:#ddd}
.foot-brand{left:180px;width:210px;height:210px;border-radius:50%;border:6px solid var(--rose);display:flex;align-items:center;justify-content:center;text-align:center;font-family:'Barlow',sans-serif;font-size:20px;font-weight:600;color:var(--rose);padding:22px;line-height:1.2;background:var(--footer)}
.foot-col h3{font-size:20px;font-weight:600;color:var(--white);margin-bottom:16px}
.foot-col a{display:block;color:#ddd;font-size:12px;text-decoration:none;line-height:1.75}
.info{display:flex;gap:18px;align-items:flex-start;font-size:12px;line-height:1.5;margin-bottom:24px}
.info svg{flex:none;margin-top:2px}
.badge{left:870px;top:150px;width:120px;height:120px;border-radius:50%;background:linear-gradient(180deg,#e0c16a,#b18a2e)}
.social{left:860px;top:300px;display:flex;gap:22px}
.social span{width:20px;height:20px;border-radius:50%;background:var(--white)}
.legal{width:1200px;text-align:center;font-size:11px;color:#ccc}
</style>
</head>
<body>

<header class="site-header">
  <div class="abs brand">Copper Ridge Harbor Home Inc.</div>
  <div class="abs topbar">
    <span class="phone"><svg width="14" height="14" viewBox="0 0 24 24"><path fill="#2f2f33" d="M6.6 10.8a15.1 15.1 0 0 0 6.6 6.6l2.2-2.2c.3-.3.7-.4 1-.2 1.1.4 2.3.6 3.6.6.6 0 1 .4 1 1V20c0 .6-.4 1-1 1A17 17 0 0 1 3 4c0-.6.4-1 1-1h3.5c.6 0 1 .4 1 1 0 1.3.2 2.5.6 3.6.1.3 0 .7-.2 1z"/></svg>CALL US: 555.014.2287</span>
    <span class="donate">DONATE NOW</span>
  </div>
  <nav class="abs nav">
    <a href="#">HOME</a><a href="#">ABOUT</a><a href="#">HOW YOU CAN HELP</a><a href="#">SERVICES OFFERED</a><a href="#">OUR LOVE OF PETS</a><a href="#">CONTACT US</a><a href="#">HARBOR WALK</a>
  </nav>
</header>

<section class="hero">
  <div class="ph" role="img" aria-label="Photo of smiling young women lying in a circle on the grass, heads together"></div>
  <svg width="1200" height="90" viewBox="0 0 1200 90" preserveAspectRatio="none"><path d="M0 30 C300 95 900 95 1200 30 L1200 90 L0 90Z" fill="#c9b7bf" opacity=".7"/><path d="M0 45 C300 105 900 105 1200 45 L1200 90 L0 90Z" fill="#f3f3f3"/></svg>
</section>

<section class="intro">
  <div class="abs intro-card" style="left:165px">
    <div class="abs" style="left:0;top:0;width:230px;text-align:right">
      <h2>OUR GIRLS</h2>
      <p>Lorem ipsum dolor sit amet, consectetur adipiscing elit, sed do eiusmod tempor incididunt ut labore et dolore mag</p>
      <span class="btn">LEARN MORE</span>
    </div>
    <div class="abs circle ph" style="left:240px;top:-5px" role="img" aria-label="Photo of a group of girls together"></div>
  </div>
  <div class="abs circle ph" style="left:615px;top:35px" role="img" aria-label="Photo of two women talking over coffee"></div>
  <div class="abs" style="left:815px;top:40px;width:230px">
    <h2 style="font-size:34px;font-weight:600;color:var(--gold);letter-spacing:1px">OUR MISSION</h2>
    <p style="font-size:12px;line-height:1.5;margin-top:8px">Lorem ipsum dolor sit amet, consectetur adipiscing elit, sed do eiusmod tempor incididunt ut labore et dolore mag</p>
    <span class="btn">LEARN MORE</span>
  </div>
</section>

<section class="about">
  <h2 class="abs">WE ARE COPPER RIDGE<br>HARBOR HOME</h2>
  <p class="abs lead">With the help of our community, we have raised over 1000 girls and counting! Some of the services we offer include:</p>
  <p class="abs body">Lorem ipsum dolor sit amet, consectetur adipiscing elit, sed do eiusmod tempor incididunt ut labore et dolore magna aliqua. Ut enim ad minim veniam, quis nostrud exercitation ullamco laboris nisi ut aliquip ex ea commodo consequat. Duis aute irure dolor in reprehenderit in voluptat</p>
  <div class="abs service" style="left:655px;top:105px">
    <svg width="56" height="56" viewBox="0 0 56 56" fill="none" stroke="#c48a9c" stroke-width="2"><path d="M28 6 46 16 28 26 10 16Z"/><path d="M10 16v22l18 10 18-10V16"/><path d="M28 26v22"/></svg>
    <span>Room, Board, and<br>Watchful Oversight</span></div>
  <div class="abs service" style="left:850px;top:105px">
    <svg width="56" height="56" viewBox="0 0 56 56" fill="none" stroke="#c48a9c" stroke-width="2"><path d="M22 44 6 28a9 9 0 0 1 16-10 9 9 0 0 1 16 10Z"/><path d="M36 44 26 34M34 20a9 9 0 0 1 16 8L36 44"/></svg>
    <span>Transitional<br>Living Services</span></div>
  <div class="abs service" style="left:655px;top:300px">
    <svg width="56" height="56" viewBox="0 0 56 56" fill="none" stroke="#c48a9c" stroke-width="2"><path d="M28 6c6 6 8 14 0 24-8-10-6-18 0-24Z"/><path d="M10 30h36v8H10zM14 38v12h28V38"/></svg>
    <span>Independent<br>Living Services</span></div>
  <div class="abs service" style="left:850px;top:300px">
    <svg width="56" height="56" viewBox="0 0 56 56" fill="none" stroke="#c48a9c" stroke-width="2"><path d="M28 46 10 28a10 10 0 0 1 18-12 10 10 0 0 1 18 12Z"/><path d="M18 30l8 6 10-10"/></svg>
    <span>Foster<br>Gift Shop</span></div>
</section>

<section class="board">
  <svg class="abs" style="top:-40px;left:0" width="1200" height="60" viewBox="0 0 1200 60" preserveAspectRatio="none"><path d="M0 60 V40 C300 0 700 0 1200 30 V60Z" fill="#f3f3f3"/></svg>
  <svg class="abs" style="left:588px;top:115px" width="24" height="22" viewBox="0 0 24 22" fill="none" stroke="#c48a9c" stroke-width="1.6"><path d="M12 20 3 11a5 5 0 0 1 9-6 5 5 0 0 1 9 6Z"/></svg>
  <h2 class="abs sec-title" style="top:148px">BOARD MEMBERS</h2>
  <p class="abs sec-sub" style="top:200px">Lorem ipsum dolor sit amet, consectetur adipiscing elit, sed do<br>eiusmod tempor incididunt ut labore et dolore magna aliqua.</p>
  <span class="abs chev" style="left:105px;top:340px">&#8249;</span>
  <span class="abs chev" style="left:1070px;top:340px">&#8250;</span>
  <div class="abs member" style="left:192px;top:300px"><div class="portrait ph" role="img" aria-label="Portrait of a board member"></div><h4>Name: Loremlsuh</h4><p>Lorem ipsum dolor sit amet, cons ctetur adipiscing elit, sed do eiusm temd tempor.</p></div>
  <div class="abs member" style="left:414px;top:300px"><div class="portrait ph" role="img" aria-label="Portrait of a board member"></div><h4>Name: Loremlsuh</h4><p>Lorem ipsum dolor sit amet, cons ctetur adipiscing elit, sed do eiusm temd tempor.</p></div>
  <div class="abs member" style="left:636px;top:300px"><div class="portrait ph" role="img" aria-label="Portrait of a board member"></div><h4>Name: Loremlsuh</h4><p>Lorem ipsum dolor sit amet, cons ctetur adipiscing elit, sed do eiusm temd tempor.</p></div>
  <div class="abs member" style="left:858px;top:300px"><div class="portrait ph" role="img" aria-label="Portrait of a board member"></div><h4>Name: Loremlsuh</h4><p>Lorem ipsum dolor sit amet, cons ctetur adipiscing elit, sed do eiusm temd tempor.</p></div>
</section>

<section class="events">
  <h2 class="abs sec-title" style="top:100px">CALENDAR OF EVENTS</h2>
  <p class="abs sec-sub" style="top:152px">Lorem ipsum dolor sit amet, consectetur adipiscing elit, sed do<br>eiusmod tempor incididunt ut labore et dolore magna aliqua.</p>
  <div class="abs card" style="left:173px">
    <div class="cal-head"><h3>MARCH</h3><div class="yr">2019</div><span class="add">ADD EVENT</span></div>
    <div class="cal-grid">
      <span class="dn">SUN</span><span class="dn">MON</span><span class="dn">TUE</span><span class="dn">WED</span><span class="dn">THU</span><span class="dn">FRI</span><span class="dn">SAT</span>
      <span class="o">24</span><span class="o">25</span><span class="o">26</span><span class="o">27</span><span class="o">28</span><span>1</span><span>2</span>
      <span>3</span><span>4</span><span>5</span><span>6</span><span style="color:var(--rose)">7</span><span>8</span><span>9</span>
      <span>10</span><span>11</span><span>12</span><span>13</span><span>14</span><span>15</span><span>16</span>
      <span>17</span><span>18</span><span>19</span><span>20</span><span>21</span><span>22</span><span>23</span>
      <span>24</span><span>25</span><span>26</span><span>27</span><span>28</span><span>29</span><span>30</span>
    </div>
  </div>
  <div class="abs card" style="left:505px">
    <div class="ph" role="img" aria-label="Photo of women laughing together at a table"></div>
    <h4>Lorem ipsum dolor sit amet, consectetur adipiscing e</h4>
    <p>Lorem ipsum dolor sit amet, consectetur adipiscing elit, sed do eiusmod tempor incididunt ut labore et dolore magna aliqua enim ad minim veniam, quis nostrud.</p>
    <span class="date">March 07 2019</span>
  </div>
  <div class="abs card" style="left:772px">
    <div class="ph" role="img" aria-label="Photo of friends gathered at a cafe"></div>
    <h4>Lorem ipsum dolor sit amet, consectetur adipiscing e</h4>
    <p>Lorem ipsum dolor sit amet, consectetur adipiscing elit, sed do eiusmod tempor incididunt ut labore et dolore magna aliqua enim ad minim veniam, quis nostrud.</p>
    <span class="date">March 07 2019</span>
  </div>
</section>

<section class="voices">
  <h2 class="abs" style="left:175px;top:95px">WHAT OUR GIRLS SAY</h2>
  <p class="abs intro-txt" style="left:175px;top:150px;width:360px">If you're a former resident of the Harbor Home and would like to tell us about your experience, please email us at hello@copperridgeharbor.org or come by and see us! You can also find us on our page, we love to hear from you.</p>
  <span class="abs" style="left:175px;top:272px;font-size:34px;font-family:'Barlow',sans-serif;font-weight:700">&ldquo;</span>
  <p class="abs quote" style="left:205px;top:282px;width:320px">I had finally hated a lot and I felt supported. I learned how to cook, budget, get a job, stay in school, join clubs, community service and helping others. I would not have gotten here without the Harbor Home.</p>
  <p class="abs quote" style="left:205px;top:383px">-Marisol</p>
  <span class="abs" style="left:200px;top:440px;font-size:24px">&#8249; &#8250;</span>
</section>

<section class="join">
  <h2 class="abs" style="left:30px;top:95px">JOIN OUR TEAM!</h2>
  <p class="abs intro-txt" style="left:30px;top:150px;width:400px">Sed ut perspiciatis unde omnis iste natus error sit voluptatem accusantium doloremque laudantium, totam rem aperiam, eaque ipsa quae ab illo inventore veritatis et quasi architecto beatae vitae dicta.</p>
  <div class="abs job" style="left:32px;top:265px"><h4>Overnight Shift<br>House Parent</h4><p>Copper Ridge | Temporary |<br>Salary: $15.00 / hour</p></div>
  <div class="abs job" style="left:277px;top:265px"><h4>Direct Care<br>Worker (DCW)</h4><p>Copper Ridge | Full-time</p></div>
</section>

<section class="contact">
  <h2 class="abs sec-title" style="left:0">CONTACT US</h2>
  <p class="abs sec-sub">Sed ut perspiciatis unde omnis iste natus error sit voluptatem accusantium doloremque laudantium, totam rem aperiam, eaque ipsa quae.</p>
  <div class="abs form">
    <div class="field">Name:</div><div class="field">Email:</div><div class="field">Phone:</div><div class="field" style="padding-bottom:40px">Message:</div>
  </div>
  <div class="abs submit">SUBMIT</div>
  <div class="abs person" role="img" aria-label="Photo of a smiling woman in a dark blazer pointing toward the form"></div>
</section>

<footer class="site-footer">
  <svg width="1200" height="60" viewBox="0 0 1200 60" preserveAspectRatio="none"><path d="M0 60 V25 C400 70 800 -10 1200 30 V60Z" fill="#3a3d43"/></svg>
  <div class="abs foot-body">
    <div class="abs foot-brand" style="top:85px">Copper Ridge Harbor Home Inc.</div>
    <div class="abs foot-col" style="left:470px;top:70px;width:140px">
      <h3>Links</h3>
      <a href="#">Home</a><a href="#">About</a><a href="#">How You Can Help</a><a href="#">Services Offered</a><a href="#">Our Love of Pets</a><a href="#">Contact Us</a><a href="#">Harbor Walk</a>
    </div>
    <div class="abs foot-col" style="left:630px;top:70px;width:220px">
      <h3>Contact Us</h3>
      <div class="info"><svg width="18" height="22" viewBox="0 0 18 22" fill="none" stroke="#ddd" stroke-width="1.6"><path d="M9 21s7-7 7-12A7 7 0 0 0 2 9c0 5 7 12 7 12Z"/><circle cx="9" cy="9" r="2.5"/></svg><span>418 Lantern Way, Copper Ridge,<br>ST 00000, USA</span></div>
      <div class="info"><svg width="18" height="18" viewBox="0 0 24 24" fill="none" stroke="#ddd" stroke-width="1.6"><path d="M6.6 10.8a15.1 15.1 0 0 0 6.6 6.6l2.2-2.2 4.6 1.5V20A17 17 0 0 1 4 4h3.5l1.3 4.6Z"/></svg><span>Phone:<br>555.014.2287</span></div>
      <div class="info"><svg width="18" height="14" viewBox="0 0 18 14" fill="none" stroke="#ddd" stroke-width="1.6"><rect x="1" y="1" width="16" height="12"/><path d="m1 1 8 7 8-7"/></svg><span>Email:<br>hello@copperridgeharbor.org</span></div>
    </div>
    <div class="abs badge" role="img" aria-label="Anniversary badge"></div>
    <div class="abs social"><span></span><span></span><span></span><span></span></div>
    <div class="abs" style="left:175px;top:350px;width:850px;border-top:1px solid #555"></div>
  </div>
  <p class="abs legal" style="top:422px">&copy; 2019 All Rights Are Reserved. Terms of Use | Privacy Policy</p>
</footer>

</body>
</html>
```